International Shipping Company requires business card designs

We are a company based in Dubai UAE with our core business being shipping and container services. Our details can be found at www.corvanlogistics.example

We are not looking for a design that necessarily involves "ships or other shipping pictures", although some reference to the business in design or colour is encouraged.

Overall design of the card must be smart and depict the company which is very professional. Fonts, colours and layout must be very contemporary in look.

```html
<!DOCTYPE html>
<html lang="en">
<head>
<meta charset="utf-8">
<title>Corvan Logistics – Business Cards</title>
<link rel="stylesheet" href="https://fonts.googleapis.com/css2?family=Roboto:wght@400;700;900&display=swap">
<style>
  :root{
    --bg:#e9ecef;
    --card:#ffffff;
    --navy:#2e2a86;
    --ocean:#0a74b8;
    --brand:#1c8fd0;
    --ink:#1f1f24;
    --muted:#3b3f8f;
  }
  *{box-sizing:border-box;margin:0;padding:0}
  html,body{width:1200px;height:951px;overflow:hidden;background:var(--bg);font-family:"Roboto",Arial,sans-serif}
  .canvas{position:relative;width:1200px;height:951px}
  .card{position:absolute;width:680px;height:390px;background:var(--card);border-radius:30px;overflow:hidden;box-shadow:0 10px 28px rgba(0,0,0,.18)}
  .card--front{left:70px;top:70px}
  .card--back{left:450px;top:500px}

  .brand{position:absolute;display:flex;align-items:center;gap:18px}
  .brand__mark{border-radius:50%;background:var(--navy);flex:none}
  .brand__name{color:var(--brand);font-weight:900;text-transform:uppercase;letter-spacing:1px;white-space:nowrap}
  .card--front .brand{left:44px;top:110px}
  .card--front .brand__mark{width:84px;height:84px}
  .card--front .brand__name{font-size:48px}
  .front__web{position:absolute;left:190px;top:262px;font-size:20px;letter-spacing:2px;color:var(--ink)}

  .card--back .brand{left:40px;top:36px;gap:12px}
  .card--back .brand__mark{width:48px;height:48px}
  .card--back .brand__name{font-size:27px}
  .back__wave{position:absolute;inset:0}
  .contact{position:absolute;left:34px;top:142px;color:var(--ink);font-size:19px;line-height:24px}
  .contact__row{display:flex;align-items:flex-start;gap:10px}
  .contact__icon{width:18px;height:18px;flex:none;margin-top:3px}
  .contact__group{margin-bottom:18px}
  .contact__list .contact__row{margin-bottom:1px}
  .person{position:absolute;right:50px;top:282px;text-align:center}
  .person__name{color:#fff;font-size:22px}
  .person__role{color:var(--muted);font-size:18px;margin-top:2px}
</style>
</head>
<body>
<main class="canvas">
  <section class="card card--front">
    <div class="brand">
      <span class="brand__mark"></span>
      <span class="brand__name">Corvan Logistics</span>
    </div>
    <p class="front__web">www.corvanlogistics.example</p>
  </section>

  <section class="card card--back">
    <svg class="back__wave" viewBox="0 0 680 390" aria-hidden="true">
      <path d="M470 0 C330 90 330 160 420 240 C480 300 470 350 430 390 L680 390 L680 0 Z" fill="var(--navy)"/>
      <path d="M510 0 C390 90 390 160 470 240 C525 300 510 350 480 390 L680 390 L680 0 Z" fill="var(--ocean)"/>
    </svg>
    <div class="brand">
      <span class="brand__mark"></span>
      <span class="brand__name">Corvan Logistics</span>
    </div>
    <div class="contact">
      <div class="contact__group contact__row">
        <svg class="contact__icon" viewBox="0 0 18 18"><path d="M9 2 L17 9 H14 V16 H4 V9 H1 Z" fill="var(--navy)"/></svg>
        <div>1450 Harbor Gate Rd<br>Portland, ME 04101</div>
      </div>
      <div class="contact__list">
        <div class="contact__row">
          <svg class="contact__icon" viewBox="0 0 18 18"><circle cx="9" cy="9" r="8" fill="none" stroke="var(--navy)" stroke-width="2"/><path d="M6 5 L8 5 L8 8 L7 9 C8 10 9 11 10 11 L11 10 L13 10 L13 12 C9 13 5 9 6 5Z" fill="var(--navy)"/></svg>
          <span>207-555-0140</span>
        </div>
        <div class="contact__row">
          <svg class="contact__icon" viewBox="0 0 18 18"><rect x="3" y="2" width="10" height="6" fill="none" stroke="var(--navy)" stroke-width="2"/><rect x="1" y="8" width="16" height="8" rx="2" fill="var(--navy)"/></svg>
          <span>207-555-0141</span>
        </div>
        <div class="contact__row">
          <svg class="contact__icon" viewBox="0 0 18 18"><rect x="1" y="4" width="16" height="11" rx="2" fill="var(--navy)"/><path d="M2 5 L9 11 L16 5" fill="none" stroke="#fff" stroke-width="1.5"/></svg>
          <span>info@corvanlogistics.example</span>
        </div>
        <div class="contact__row">
          <svg class="contact__icon" viewBox="0 0 18 18"><circle cx="9" cy="9" r="8" fill="var(--navy)"/></svg>
          <span>www.corvanlogistics.example</span>
        </div>
      </div>
    </div>
    <div class="person">
      <p class="person__name">Marek Tolliver</p>
      <p class="person__role">director</p>
    </div>
  </section>
</main>
</body>
</html>
```